Property Finance Company - Orca Ridge Limited

Background: Orca Ridge Group Limited is a private property finance company. Orca Ridge Group has capital to directly fund first mortgage, mezzanine and preferred equity financing. We also acquire performing, sub-performing and distressed debt.

Orca Ridges management philosophy emphasises expertise, innovation, wisdom, honesty and competitiveness. Orca Ridge are not finance brokers - we provide debt funding to the commercial property and residential development sectors. Our process is built from experience and cumutavely Orca Ridges Directors have in excess of 60 years wisdom.

The aim of the website will be to increase brand awareness, provide clients with comfort around our level of skill and background on who we are, generate more sales, and provide examples of projects that we have funded.

The website is a new product launch, and we need to use our Orca Ridge logo that has just been designed. We like a dark background, and either black/silver/grey/ jade green, or black/gold/jade green colours.

Our unique advantages are that we have fast turnaround times, we can solve clients funding problems and we know what we are doing. Our target audience will be viewing the website on both desktop and mobile devices.

We would like to have the following pages:

Home
About
Team
Services
Project Experience
Contact

Competitors Website: http://www.vbtq.example/

We would also like to have the option of video footage in our website, as you can see in our competitors website.

Overall we want a really slick, elegant but modern website that is better than www.vbtq.example

Target Market(s)

Finance borrowers, property developers, accountants, lawyers, businesspeople, high net worth people

Industry/Entity Type

Finance

Requirements
Must have
• Please see project description
Nice to have
Should not have

```html
<!DOCTYPE html>
<html lang="en">
<head>
<meta charset="utf-8">
<title>Orca Ridge Group</title>
<link href="https://fonts.googleapis.com/css2?family=Cinzel:wght@400&family=Montserrat:wght@400;500;600&family=Poppins:wght@500&family=Crimson+Text:ital@1&display=swap" rel="stylesheet">
<style>
  :root {
    --page: #ffffff;
    --ink: #3a3a3a;
    --heading: #44524c;
    --muted: #8a8a8a;
    --jade: #3f9a7a;
    --hero-dark: #2a2c2e;
    --hero-mid: #6d7175;
    --hero-light: #a9adb0;
    --white: #ffffff;
  }
  * { box-sizing: border-box; margin: 0; padding: 0; }
  html, body { width: 752px; height: 1200px; overflow: hidden; background: var(--page); }
  body { position: relative; font-family: "Montserrat", sans-serif; color: var(--ink); }

  .hero {
    position: absolute; left: 8px; top: 8px; width: 736px; height: 458px;
    background: linear-gradient(180deg, var(--hero-light) 0%, var(--hero-mid) 45%, var(--hero-dark) 100%);
  }
  .brand-mark {
    position: absolute; left: 60px; top: 38px;
    display: flex; align-items: center; gap: 8px;
    font-family: "Cinzel", serif; font-size: 14px; color: var(--white);
  }
  .brand-mark .dot { width: 12px; height: 12px; border-radius: 50%; background: var(--white); }
  .menu-toggle { position: absolute; right: 58px; top: 44px; }
  .hero-title {
    position: absolute; left: 0; right: 0; top: 200px; text-align: center;
    font-family: "Cinzel", serif; font-weight: 400; font-size: 44px; line-height: 1.2;
    color: var(--white); letter-spacing: 1px;
  }

  .section-label {
    position: absolute; left: 18px;
    font-size: 15px; font-weight: 500; letter-spacing: 1.2px; color: #555;
  }
  .about-label { top: 492px; }
  .about-nav {
    position: absolute; left: 33px; top: 576px; list-style: none;
    font-family: "Crimson Text", serif; font-style: italic; font-size: 12px; line-height: 19px; color: #777;
  }
  .about-heading {
    position: absolute; left: 156px; top: 520px; width: 520px;
    font-family: "Poppins", sans-serif; font-weight: 500; font-size: 31px; line-height: 38px; color: var(--heading);
  }
  .about-copy {
    position: absolute; left: 157px; top: 622px; width: 585px;
    font-family: "Crimson Text", serif; font-style: italic; font-size: 11.5px; line-height: 20px; color: var(--muted);
  }
  .about-copy p + p { margin-top: 14px; }

  .services-label { top: 786px; }
  .service {
    position: absolute; top: 838px; width: 200px; text-align: center;
  }
  .service-photo { width: 156px; height: 156px; border-radius: 50%; margin: 0 auto; }
  .photo-cranes { background: linear-gradient(160deg, #d9e2ea 0%, #b9c7d1 60%, #c8873e 100%); }
  .photo-bridge { background: linear-gradient(170deg, #eef1f3 0%, #9aa6b0 55%, #5b6670 100%); }
  .photo-tower { background: linear-gradient(160deg, #cfdde5 0%, #e8edf0 55%, #b7c2c9 100%); }
  .service-title {
    margin-top: 30px; font-size: 12px; font-weight: 600; letter-spacing: 0.4px; color: #333;
  }
  .service-text {
    margin: 22px auto 0; width: 180px;
    font-size: 8.6px; line-height: 16px; color: var(--muted);
  }
  .read-more {
    display: block; margin-top: 8px;
    font-family: "Crimson Text", serif; font-style: italic; font-size: 10px; color: var(--jade); text-decoration: none;
  }
</style>
</head>
<body>
  <header class="hero" role="img" aria-label="Photo: silhouetted business people at tall office windows overlooking a city skyline">
    <div class="brand-mark"><span class="dot"></span>Orca Ridge</div>
    <svg class="menu-toggle" width="14" height="11" viewBox="0 0 14 11" aria-hidden="true">
      <rect y="0" width="14" height="2" fill="#fff"/>
      <rect y="4.5" width="14" height="2" fill="#fff"/>
      <rect y="9" width="14" height="2" fill="#fff"/>
    </svg>
    <h1 class="hero-title">Orca Ridge<br>Group</h1>
  </header>

  <h2 class="section-label about-label">ABOUT US</h2>
  <ul class="about-nav">
    <li>Philosophy</li>
    <li>Expertise</li>
    <li>Vision</li>
  </ul>
  <h3 class="about-heading">In faucibus dui quis libero faucis, euismod dolor mattis</h3>
  <div class="about-copy">
    <p>Pellentesque maximus, nisl vel rutrum semper, nibh nisl mollis leo, eu euismod tortor tellus vestibulum dui. Fusce non eleifend mi. In accumsan sapien eget nibh rutrum tincidunt. Curabitur sit amet felis sit amet ex cursus mollis et in sem. Maecenas sit amet pellentesque arcu. Pellentesque feugiat, ligula id rutrum condimentum, leo dolor porttitor eros, vel placerat tellus mauris nec leo.</p>
    <p>Sed eu euismod libero, ut eleifend justo. Aliquam consequat, lacus vel mollis gravida, purus eros porttitor enim, scelerisque efficitur neque sem sit amet ex. Donec tincidunt mollis volutpat. Nunc id hendrerit nulla, in mattis sem. Cras</p>
  </div>

  <h2 class="section-label services-label">OUR SERVICES</h2>

  <section class="service" style="left:60px">
    <div class="service-photo photo-cranes" role="img" aria-label="Photo: construction cranes against a pale sky"></div>
    <h4 class="service-title">DEVELOPMENT FINANCE</h4>
    <p class="service-text">Fusce sodales neque eu lacinia dapibus. Nunc aliquam eget orci in fermentum. Aliquam eros nibh, varis non ipsum vitae, rutrum hendrit senectus et netus et malesuda.</p>
    <a class="read-more" href="#">Read more</a>
  </section>

  <section class="service" style="left:276px">
    <div class="service-photo photo-bridge" role="img" aria-label="Photo: underside of a long concrete bridge"></div>
    <h4 class="service-title">BRIDGING FINANCE</h4>
    <p class="service-text">Fusce sodales neque eu lacinia dapibus. Nunc aliquam in varis ipsum vitae, rutrum hedrit lectus. Pelentesque habitan morbi tristue senectus et netus et malesuda fams ac turpisegestas.</p>
    <a class="read-more" href="#">Read more</a>
  </section>

  <section class="service" style="left:491px">
    <div class="service-photo photo-tower" role="img" aria-label="Photo: modern white apartment tower"></div>
    <h4 class="service-title">BANK FINANCE</h4>
    <p class="service-text">Fusce sodales neque eu lacinia dapibus. Nunc aliquam eget orci in fermentum. Aliquam eros nibh, varis non ipsum vitae, rutrum hendrit senectus et netusurpisegestas.</p>
    <a class="read-more" href="#">Read more</a>
  </section>
</body>
</html>
```